Brochure about Gun Trusts

Cover Page: Image of a firearm collection or a lockbox with the title]
Headline: Protect Your Firearms Collection with a Gun Trust
Subheading: Ensure Your Legacy Remains Private and Your Wishes Are Respected
[Page 1: What is a Gun Trust?]
Definition: A legally recognized trust that allows you to collect, own, and transfer firearms, including those restricted by the NFA.
Quote: "A gun trust is a revocable trust created to hold ownership of a firearm..." - QMR
[Page 2: Benefits of a Gun Trust]
Avoid Probate: Keep your firearms out of the public probate process, maintaining your privacy.
Multi-Generational Ownership: Easily transfer ownership to beneficiaries without the need for a court proceeding.
Shared Responsibility: Allow others to legally possess and use the firearms held in the trust.
[Page 3: The Risks of Not Having a Gun Trust]
Inheritance Issues: Firearms may not be transferred as intended, potentially leading to legal complications.
Probate and Public Disclosure: Your firearms collection becomes a public record.
[Page 4: How to Set Up a Gun Trust]
Consult with an Attorney: A firearms trust attorney will create a trust that complies with all federal and state laws.
Assign a Trustee: Choose a trustee to manage the trust if you become incapacitated or pass away.
Transfer Ownership: Assign your firearms to the trust.
[Back Cover: Call to Action]
Headline: Protect Your Firearms Legacy
Contact Information: Address, Phone Number, Email, Website
Offer: Free Consultation to discuss your options

```html
<!DOCTYPE html>
<html lang="en">
<head>
<meta charset="utf-8">
<title>Gun Trust Brochure</title>
<link href="https://fonts.googleapis.com/css2?family=Montserrat:ital,wght@0,400;0,600;0,700;0,800;1,800;1,900&display=swap" rel="stylesheet">
<style>
:root{
  --red:#d3161c;
  --red-dark:#8e0f13;
  --ink:#141414;
  --ink-2:#1e1e1e;
  --paper:#ffffff;
  --stage:#e9e9ea;
  --grey:#bdbdbd;
  --muted:#8a8a8a;
}
*{box-sizing:border-box;margin:0;padding:0}
html,body{width:1200px;height:2244px;overflow:hidden;background:var(--stage);font-family:"Montserrat",Arial,sans-serif}
.page{position:absolute;width:500px;height:680px;overflow:hidden;background:var(--ink);color:var(--paper);box-shadow:0 2px 6px rgba(0,0,0,.25)}
.p-cover{left:88px;top:88px}
.p-back{left:612px;top:88px}
.p-what{left:88px;top:792px}
.p-benefits{left:612px;top:792px}
.p-risks{left:88px;top:1496px}
.p-howto{left:612px;top:1496px;background:var(--paper);color:var(--ink)}
.photo{position:absolute}
.head{font-weight:900;font-style:italic;text-transform:uppercase;line-height:.95;letter-spacing:-.5px}
.red{color:var(--red)}
.site{position:absolute;left:0;right:0;bottom:26px;text-align:center;font-weight:700;font-size:17px;letter-spacing:.5px}
.footer{position:absolute;left:34px;right:34px;bottom:24px;display:flex;justify-content:space-between;align-items:center;font-size:11px;color:var(--grey)}
.footer .tab{width:26px;height:16px;background:var(--red)}
/* cover */
.cover-title{position:absolute;top:50px;left:0;right:0;text-align:center}
.cover-title .l1{font-size:34px;color:var(--red)}
.cover-title .l2{font-size:48px}
.cover-title .l3{font-size:30px;white-space:nowrap;margin-top:4px}
.cover-title .l3 .red{font-size:44px}
.cover-sub{position:absolute;left:60px;right:60px;top:500px;text-align:center;font-weight:800;font-size:17px;line-height:1.3;text-transform:uppercase}
/* back */
.consult{position:absolute;left:34px;top:405px}
.consult .big{font-size:44px;font-weight:800;line-height:1}
.consult .tag{display:inline-block;margin-top:8px;background:var(--red);padding:5px 10px;font-size:10px;font-weight:700;letter-spacing:.5px}
.contact{position:absolute;left:268px;top:400px;list-style:none}
.contact li{display:flex;align-items:flex-start;gap:10px;font-size:12px;margin-bottom:16px;color:#e6e6e6;line-height:1.35}
.contact svg{flex:none}
/* what */
.what-head{position:absolute;left:34px;top:50px;font-size:30px;white-space:nowrap}
.what-def{position:absolute;left:34px;right:40px;top:96px;font-size:17px;line-height:1.35}
.what-def b{color:var(--red)}
.quote{position:absolute;left:34px;top:218px;width:240px;background:var(--red);padding:22px 20px 20px;font-size:15px;font-weight:700;line-height:1.35}
.quote .qm{position:absolute;font-size:48px;font-weight:900;line-height:1}
.quote .by{display:block;margin-top:8px;font-weight:400}
/* benefits */
.ben-panel{position:absolute;left:240px;top:0;width:260px;height:680px;background:var(--paper);color:var(--ink);padding:48px 22px 0 22px}
.ben-panel .head{font-size:38px}
.ben-item{margin-top:26px}
.ben-item .lab{display:block;background:var(--red);color:#fff;font-size:10px;font-weight:800;padding:5px 8px;text-transform:uppercase}
.ben-item p{font-size:11px;line-height:1.4;margin-top:6px;padding-left:2px}
/* risks */
.risk-head{position:absolute;left:34px;top:44px;font-size:30px;white-space:nowrap}
.risk-box{position:absolute;background:var(--red);padding:12px 14px;width:200px}
.risk-box h3{font-size:15px;font-weight:800;font-style:italic}
.risk-box p{font-size:10.5px;line-height:1.4;margin-top:6px}
/* how to */
.how-head{position:absolute;left:30px;top:46px;font-size:44px;color:var(--ink);width:240px}
.how-col{position:absolute;left:298px;top:0;width:202px;height:500px;background:var(--red-dark);color:#fff;padding:44px 18px 0}
.how-item{margin-bottom:28px}
.how-item h3{font-size:12px;font-weight:800;color:#ff5a5e}
.how-item p{font-size:11px;line-height:1.4;margin-top:4px}
</style>
</head>
<body>

<section class="page p-cover">
  <div class="photo" role="img" aria-label="Dark textured background with scattered firearms" style="inset:0;background:radial-gradient(ellipse at 50% 60%,#2c2c2c,#0d0d0d 75%)"></div>
  <div class="cover-title head">
    <div class="l1">Protect Your</div>
    <div class="l2">Firearms</div>
    <div class="l2">Collection</div>
    <div class="l3">With A <span class="red">Gun Trust</span></div>
  </div>
  <div class="photo" role="img" aria-label="Handgun resting in an open lockbox" style="left:90px;top:300px;width:320px;height:180px;background:linear-gradient(160deg,#4a4a4a,#1b1b1b);border-radius:4px"></div>
  <p class="cover-sub">Ensure your legacy remains private and your wishes are respected</p>
  <div class="site">www.ArmoryLegacy.com</div>
</section>

<section class="page p-back">
  <div class="photo" role="img" aria-label="Handguns and ammunition laid on a dark surface" style="left:0;top:0;width:500px;height:370px;background:linear-gradient(180deg,#5a5a5a,#262626 80%,#141414)"></div>
  <div class="consult">
    <div class="big">FREE</div>
    <div class="big" style="font-size:24px">CONSULTATION</div>
    <span class="tag">TO DISCUSS YOUR OPTIONS</span>
  </div>
  <ul class="contact">
    <li><svg width="18" height="18" viewBox="0 0 24 24"><circle cx="12" cy="12" r="12" fill="#d3161c"/><path d="M8 6l2.5 2-1 2a8 8 0 0 0 4.5 4.5l2-1 2 2.5-2 2A11 11 0 0 1 6 8z" fill="#fff"/></svg>000 555 0148</li>
    <li><svg width="18" height="18" viewBox="0 0 24 24"><circle cx="12" cy="12" r="12" fill="#d3161c"/><rect x="6" y="8" width="12" height="8" fill="none" stroke="#fff" stroke-width="1.5"/><path d="M6 8l6 5 6-5" fill="none" stroke="#fff" stroke-width="1.5"/></svg>hello@armorylegacy.com</li>
    <li><svg width="18" height="18" viewBox="0 0 24 24"><circle cx="12" cy="12" r="12" fill="#d3161c"/><path d="M12 5a4.5 4.5 0 0 0-4.5 4.5C7.5 13 12 19 12 19s4.5-6 4.5-9.5A4.5 4.5 0 0 0 12 5z" fill="#fff"/><circle cx="12" cy="9.5" r="1.6" fill="#d3161c"/></svg><span>1200 Oak Lane,<br>Springfield, ST 00000</span></li>
  </ul>
  <div class="site">www.ArmoryLegacy.com</div>
</section>

<section class="page p-what">
  <div class="what-head head">What is a <span class="red">Gun Trust</span>?</div>
  <p class="what-def">A legally recognized trust that allows you to <b>collect, own, and transfer firearms</b>, including those restricted by the NFA.</p>
  <div class="quote">
    <span class="qm" style="left:10px;top:-14px">“</span>
    A gun trust is a revocable trust created to hold ownership of a firearm...
    <span class="by">- QMR</span>
    <span class="qm" style="right:10px;bottom:-26px">”</span>
  </div>
  <div class="photo" role="img" aria-label="Revolver and handgun with loose cartridges" style="left:150px;top:390px;width:320px;height:200px;background:radial-gradient(ellipse at 50% 50%,#565656,#1a1a1a 70%)"></div>
  <div class="footer"><span>www.trustarmory.com</span><span class="tab"></span></div>
</section>

<section class="page p-benefits">
  <div class="photo" role="img" aria-label="Close-up of a handgun and bullets on a dark table" style="left:0;top:0;width:240px;height:680px;background:linear-gradient(160deg,#3d3d3d,#111)"></div>
  <div class="ben-panel">
    <div class="head">Benefits<br>of a <span class="red">Gun<br>Trust</span></div>
    <div class="ben-item"><span class="lab">Avoid Probate</span><p>Keep your firearms out of the public probate process, maintaining your privacy.</p></div>
    <div class="ben-item"><span class="lab">Multi-Generational Ownership</span><p>Easily transfer ownership to beneficiaries without the need for a court proceeding.</p></div>
    <div class="ben-item"><span class="lab">Shared Responsibility</span><p>Allow others to legally possess and use the firearms held in the trust.</p></div>
  </div>
  <div class="footer" style="left:262px"><span style="color:#777">www.trustarmory.com</span><span class="tab"></span></div>
</section>

<section class="page p-risks">
  <div class="risk-head head"><span class="red">The Risks of</span><br><span class="red">Nothaving a</span> Gun Trust</div>
  <div class="photo" role="img" aria-label="Collector reviewing documents beside a gun safe" style="left:34px;top:140px;width:220px;height:170px;background:linear-gradient(160deg,#5a4a3e,#1e1a17)"></div>
  <div class="risk-box" style="left:262px;top:170px"><h3>Inheritance Issues:</h3><p>Firearms may not be transferred as intended, potentially leading to legal complications.</p></div>
  <div class="risk-box" style="left:34px;top:360px"><h3>Probate and Public Disclosure:</h3><p>Your firearms collection becomes a public record.</p></div>
  <div class="photo" role="img" aria-label="Courtroom interior with wooden benches" style="left:250px;top:340px;width:216px;height:250px;background:linear-gradient(180deg,#6b4a30,#2a1c12)"></div>
  <div class="footer"><span>www.trustarmory.com</span><span class="tab"></span></div>
</section>

<section class="page p-howto">
  <div class="how-head head">What is a <span class="red">How to set up a Gun Trust?</span></div>
  <div class="how-col">
    <div class="how-item"><h3>Consult with an Attorney:</h3><p>A firearms trust attorney will create a trust that complies with all federal and state laws.</p></div>
    <div class="how-item"><h3>Assign a Trustee:</h3><p>Choose a trustee to manage the trust if you become incapacitated or pass away.</p></div>
    <div class="how-item"><h3>Transfer Ownership:</h3><p>Assign your firearms to the trust.</p></div>
  </div>
  <div class="photo" role="img" aria-label="Black handgun with scattered cartridges" style="left:0;top:300px;width:298px;height:380px;background:linear-gradient(180deg,#f2f2f2,#9a9a9a 55%,#2a2a2a)"></div>
  <div class="photo" role="img" aria-label="Hands signing trust documents at a desk" style="left:298px;top:500px;width:202px;height:180px;background:linear-gradient(160deg,#8a6a4e,#3a2a1e)"></div>
</section>

</body>
</html>
```